Salon and Spa Distributor Business Card

Need a business card. We are are distributor in the salon and spa industry. We identify with natural beauty. Need a card with:
Company Name: Petal Haven"
Title: "President & CEO"
Address
Company Phone number
email
website
Tag Line:" Naturally Yours, Salon to Spa"

Industry/Entity Type

Business

Contact Information for Business Card

Name: Lena Morcott
Title: "President & CEO"
Address: 317 Birchfield Ln, Oakvane, NJ 07481
Company Phone number: 800-463-9152
email: lenamorcott@petalhaven-example.com
website: www.petalhaven-example.com

Requirements
Should not have
• No black backgrounds

```html
<!DOCTYPE html>
<html lang="en">
<head>
<meta charset="utf-8">
<title>Petal Haven Business Card</title>
<link href="https://fonts.googleapis.com/css2?family=Arimo:wght@400;500;700&family=Questrial&display=swap" rel="stylesheet">
<style>
  :root {
    --page: #ffffff;
    --mint: #c0e3c8;
    --leaf: #3f9a48;
    --band-light: #58a767;
    --paper: #f1f1f0;
    --forest: #1d4a14;
    --ink: #1a3d10;
    --white: #ffffff;
  }
  * { box-sizing: border-box; margin: 0; padding: 0; }
  html, body { width: 1200px; height: 1200px; overflow: hidden; background: var(--page); }
  .canvas { position: relative; width: 1200px; height: 1200px; }
  .card { position: absolute; width: 722px; height: 435px; overflow: hidden; }
  .card--front { left: 239px; top: 106px; background: var(--mint); }
  .card--back { left: 240px; top: 628px; background: var(--paper); }

  .brand { position: absolute; display: flex; align-items: center; gap: 14px; font-family: "Questrial", sans-serif; color: var(--leaf); white-space: nowrap; }
  .brand__dot { border-radius: 50%; background: var(--leaf); flex: none; }
  .card--front .brand { left: 50%; top: 190px; transform: translateX(-50%); font-size: 38px; }
  .card--front .brand__dot { width: 44px; height: 44px; }
  .card--back .brand { left: 50%; top: 72px; transform: translateX(-50%); font-size: 28px; }
  .card--back .brand__dot { width: 34px; height: 34px; }

  .band { position: absolute; left: 0; right: 0; bottom: 0; display: flex; align-items: center; justify-content: center; color: var(--white); white-space: nowrap; }
  .band--web { height: 40px; background: var(--band-light); font-family: "Arimo", sans-serif; font-weight: 700; font-size: 22px; letter-spacing: 3px; }
  .band--tagline { height: 36px; background: var(--forest); font-family: "Questrial", sans-serif; font-size: 19px; letter-spacing: 1.5px; }

  .person { position: absolute; left: 74px; top: 240px; color: var(--ink); font-family: "Arimo", sans-serif; white-space: nowrap; }
  .person__name { font-size: 38px; font-weight: 400; line-height: 1; letter-spacing: 0.3px; -webkit-text-stroke: 0.6px var(--ink); }
  .person__title { margin-top: 4px; font-size: 15px; font-weight: 700; letter-spacing: 7.4px; }

  .contacts { position: absolute; left: 392px; top: 214px; list-style: none; font-family: "Arimo", sans-serif; font-weight: 500; color: var(--ink); }
  .contacts__item { display: flex; align-items: center; gap: 16px; height: 30px; font-size: 15.5px; white-space: nowrap; }
  .contacts__icon { width: 25px; height: 25px; flex: none; }
  .address { position: absolute; left: 392px; top: 322px; font-family: "Arimo", sans-serif; font-weight: 500; font-size: 16px; color: var(--ink); white-space: nowrap; }
</style>
</head>
<body>
<main class="canvas">
  <section class="card card--front" aria-label="Card front">
    <div class="brand"><span class="brand__dot"></span><span class="brand__name">Petal Haven</span></div>
    <div class="band band--web">www.petalhaven-example.com</div>
  </section>

  <section class="card card--back" aria-label="Card back">
    <div class="brand"><span class="brand__dot"></span><span class="brand__name">Petal Haven</span></div>

    <div class="person">
      <h1 class="person__name">Lena Morcott</h1>
      <p class="person__title">President &amp; CEO</p>
    </div>

    <ul class="contacts">
      <li class="contacts__item">
        <svg class="contacts__icon" viewBox="0 0 24 24" aria-hidden="true">
          <circle cx="12" cy="12" r="10.5" fill="none" stroke="var(--forest)" stroke-width="1.5"/>
          <rect x="6.5" y="8.5" width="11" height="7.5" fill="var(--forest)"/>
          <path d="M6.5 8.5 L12 13 L17.5 8.5" fill="none" stroke="var(--paper)" stroke-width="1"/>
        </svg>
        <span>lenamorcott@petalhaven-example.com</span>
      </li>
      <li class="contacts__item">
        <svg class="contacts__icon" viewBox="0 0 24 24" aria-hidden="true">
          <circle cx="12" cy="12" r="10.5" fill="none" stroke="var(--forest)" stroke-width="1.5"/>
          <path d="M8.2 6.5 L10 6.2 L11 9.2 L9.8 10.3 C10.5 12 11.8 13.4 13.6 14.2 L14.7 13 L17.6 14 L17.4 15.9 C17.3 16.8 16.4 17.4 15.5 17.2 C11 16.2 7.6 12.8 6.7 8.4 C6.6 7.4 7.2 6.6 8.2 6.5 Z" fill="var(--forest)"/>
        </svg>
        <span>800-463-9152</span>
      </li>
      <li class="contacts__item">
        <svg class="contacts__icon" viewBox="0 0 24 24" aria-hidden="true">
          <circle cx="12" cy="12" r="10.5" fill="none" stroke="var(--forest)" stroke-width="1.5"/>
          <circle cx="12" cy="12" r="5.5" fill="var(--forest)"/>
          <path d="M6.5 12 H17.5 M12 6.5 V17.5 M8 9.5 H16 M8 14.5 H16" stroke="var(--paper)" stroke-width="0.8"/>
          <ellipse cx="12" cy="12" rx="2.4" ry="5.5" fill="none" stroke="var(--paper)" stroke-width="0.8"/>
        </svg>
        <span>www.petalhaven-example.com</span>
      </li>
    </ul>

    <p class="address">317 Birchfield Ln, Oakvane, NJ 07481</p>

    <div class="band band--tagline">Naturally Yours, Salon to Spa</div>
  </section>
</main>
</body>
</html>
```